TZ BLOOM
transformative skincare
plant-based | clean | anti-aging
The line is for both men and women
-luxurious feeling, plant-based, all natural skincare line
This is a continuation from previous project but maybe with sans serif or serif font instead of cursive for the ML part of Bloom. (Please see logo designs from 2 years ago)
- I think TZ Bloom should be smaller in size than the names of the product so people can more easily read what it says since there are a lot of products in a set.
Also, the day products will have very light cream almost white colored labels with dark green and gold fonts/accents and the night products will have dark green almost black labels with light cream and gold colored font I think.

The products are for both men and women so I don't want the labels looking too feminine? Maybe more simple or a faint leaf design in background.

-about 24 different labels for skincare jars and bottles:
Glycolic Cleanser 4oz and 8oz
Cleansing Oil 4oz and 8oz
Vitamin C Day Serum 1oz and 2oz
Stem Cell C Day Serum 1oz and 2oz
Stem Cell Day Cream 2oz and 4oz
Retinol Night Serum - Lavender 1oz and 2oz
Retinol Night Serum - Neroli 1oz and 2oz
Coconut Charcoal Scrub 2oz and 4oz
Enzyme Night Cream 2oz and 4oz
Eye Renewal Night Serum .5oz
Vitamin C Day Eye Cream .5oz
Honey Lip Balm .5oz
Enzyme Body Lotion - Vanilla Almond 8oz
Enzyme Body Lotion - Mango Lime 8oz
Enzyme Body Lotion - Lavender 8oz

Target Market(s)

ages 40-50 with some 20's and 30's sprinkled in

Industry/Entity Type

Beauty and Skincare

Font styles to use
Serif
Sans Serif
Other font styles liked:
• If you have a more unique but clean or slick font or combo of fonts in mind, please be creative!

Colors
00AB8E
00BBA5
67D7C9
C6EFE9
E9F9F6
FFF300
FFF600
FEFA6F
FFFEC7
FFFEE8

Requirements
Must have
• TZ Bloom should be smaller in size than the names of the product so people can more easily read what it says since there are a lot of products in a set. day products will be light colored labels with dark green and gold fonts/accents and the night products will be on dark green labels with light cream and gold colored font
Nice to have
• Attached are original files of a logo previously designed a couple years ago but not sure I want the script ML anymore? Some sort of leaf design to go with previously made logo but want to see ML in serif or sans serif instead of script. Also attached are simple labels on the products currently and how they look as they're being sold to private clients. Wanting to put them out online for the public this year so need high end, luxurious look and feel but not generic. Thank you!
Should not have
• too busy of a design

```html
<!DOCTYPE html>
<html lang="en">
<head>
<meta charset="utf-8">
<title>TZ Bloom Serum Labels</title>
<link href="https://fonts.googleapis.com/css2?family=Cinzel:wght@400;500&family=Montserrat:wght@500&display=swap" rel="stylesheet">
<style>
  :root {
    --canvas-bg: #e4e2dd;
    --night-green: #1f4a35;
    --day-cream: #f6f3ec;
    --gold: #b88c57;
    --gold-light: #c9a272;
    --deep-green: #2f5a48;
    --leaf-night: rgba(190, 200, 170, 0.14);
    --leaf-day: rgba(150, 165, 155, 0.18);
  }
  * { margin: 0; padding: 0; box-sizing: border-box; }
  html, body {
    width: 1200px;
    height: 800px;
    overflow: hidden;
    background: var(--canvas-bg);
  }
  .label-set {
    position: relative;
    width: 1200px;
    height: 800px;
    display: flex;
    justify-content: center;
    align-items: center;
    gap: 80px;
  }
  .label {
    position: relative;
    width: 440px;
    height: 540px;
    display: flex;
    flex-direction: column;
    align-items: center;
    overflow: hidden;
  }
  .label--night { background: var(--night-green); }
  .label--day { background: var(--day-cream); }
  .leaf-motif {
    position: absolute;
    left: 90px;
    top: 40px;
    width: 260px;
    height: 460px;
    border-radius: 50% 50% 50% 50% / 60% 60% 40% 40%;
  }
  .label--night .leaf-motif {
    background: radial-gradient(ellipse at center, var(--leaf-night), transparent 70%);
  }
  .label--day .leaf-motif {
    background: radial-gradient(ellipse at center, var(--leaf-day), transparent 70%);
  }
  .brand-name {
    position: relative;
    margin-top: 108px;
    font-family: "Montserrat", sans-serif;
    font-weight: 500;
    font-size: 24px;
    letter-spacing: 0.08em;
  }
  .label--night .brand-name { color: var(--gold); }
  .label--day .brand-name { color: var(--deep-green); }
  .product-name {
    position: relative;
    margin-top: 72px;
    font-family: "Cinzel", serif;
    font-weight: 500;
    font-size: 40px;
    line-height: 1.3;
    text-align: center;
    color: var(--gold-light);
  }
  .label--day .product-name { color: var(--gold); }
  .product-scent {
    position: relative;
    margin-top: 10px;
    font-family: "Montserrat", sans-serif;
    font-weight: 500;
    font-size: 20px;
    color: var(--gold);
  }
  .product-size {
    position: absolute;
    bottom: 28px;
    left: 0;
    right: 0;
    text-align: center;
    font-family: "Cinzel", serif;
    font-size: 16px;
    color: var(--gold);
  }
</style>
</head>
<body>
  <main class="label-set">
    <section class="label label--night">
      <div class="leaf-motif" role="img" aria-label="Faint botanical leaf sprig decoration"></div>
      <div class="brand-name">TZ BLOOM</div>
      <h1 class="product-name">Retinol<br>Night Serum</h1>
      <p class="product-scent">Neroli</p>
      <p class="product-size">2oz</p>
    </section>
    <section class="label label--day">
      <div class="leaf-motif" role="img" aria-label="Faint botanical leaf sprig decoration"></div>
      <div class="brand-name">TZ BLOOM</div>
      <h1 class="product-name">Vitamin C<br>Day Serum</h1>
      <p class="product-size">2oz</p>
    </section>
  </main>
</body>
</html>
```